Advertisements for dental office (3"x3.75" and 3"x2")
People of all ages looking for a family dentist.
I am looking for advertisements that are clean and sophisticated. Most dental ads are cluttered looking and list all the procedures that a dentist will perform. I do not want clutter. I want an ad that speaks for itself and has a lot of emotional appeal. The ads should be simple but still catch your eye.

```html
<!DOCTYPE html>
<html lang="en">
<head>
<meta charset="utf-8">
<title>Dental Office Advertisements</title>
<link href="https://fonts.googleapis.com/css2?family=PT+Sans+Narrow:wght@400;700&family=Cormorant+SC:wght@600&display=swap" rel="stylesheet">
<style>
  :root {
    --page-bg: #e9e6e1;
    --card-bg: #ffffff;
    --plum: #7b1f3f;
    --plum-deep: #5e1530;
    --sky: #5cbde9;
    --sky-deep: #2e9fd8;
    --white: #ffffff;
    --muted: #8a7a80;
    --photo-warm: #d9b8a0;
    --photo-cool: #7ea6cf;
    --photo-coral: #e2866b;
  }
  * { box-sizing: border-box; margin: 0; padding: 0; }
  html, body {
    width: 1200px; height: 580px; overflow: hidden;
    background: var(--page-bg);
    font-family: "PT Sans Narrow", "Arial Narrow", sans-serif;
  }
  .ad-set {
    position: relative; width: 1200px; height: 580px;
    display: flex; justify-content: center; align-items: center; gap: 50px;
  }
  .ad {
    position: relative; width: 540px; height: 410px;
    background: var(--card-bg);
    overflow: hidden;
    box-shadow: 0 6px 18px rgba(0,0,0,0.18);
  }
  .ad__band {
    position: absolute; left: 0; top: 0; width: 100%; height: 118px;
    padding: 18px 26px 0 0;
    text-align: right; color: var(--white);
  }
  .ad--plum .ad__band { background: var(--plum); }
  .ad--sky .ad__band { background: linear-gradient(180deg, var(--sky) 0%, var(--sky-deep) 100%); }
  .ad__headline { font-size: 38px; font-weight: 700; line-height: 1.05; }
  .ad__subhead { font-size: 34px; font-weight: 400; line-height: 1.1; }
  .ad__photo {
    position: absolute; left: 0; top: 118px; width: 330px; height: 292px;
    background: radial-gradient(ellipse at 40% 35%, var(--photo-warm) 0%, var(--photo-cool) 55%, var(--photo-coral) 100%);
  }
  .ad__practice {
    position: absolute; right: 12px; top: 150px; width: 196px;
    display: flex; flex-direction: column; align-items: center; text-align: center;
  }
  .ad__mark {
    width: 40px; height: 40px; border-radius: 50%;
    background: var(--plum); margin-bottom: 8px;
  }
  .ad__name {
    font-family: "Cormorant SC", Georgia, serif;
    font-weight: 600; font-size: 14px; color: var(--plum);
    white-space: nowrap;
  }
  .ad__tagline { font-size: 9px; color: var(--muted); margin-top: 2px; }
  .ad__contact {
    position: absolute; right: 22px; bottom: 24px;
    text-align: right; color: var(--plum-deep);
    font-style: normal; font-size: 17px; line-height: 1.25;
  }
  .ad__phone { font-weight: 700; }
</style>
</head>
<body>
<main class="ad-set">
  <article class="ad ad--plum">
    <header class="ad__band">
      <h1 class="ad__headline">A Beautiful Smile</h1>
      <p class="ad__subhead">Today, It's Easier Than Ever</p>
    </header>
    <div class="ad__photo" role="img" aria-label="Photograph of a smiling older couple embracing, man in a blue shirt and woman in a coral top"></div>
    <div class="ad__practice">
      <span class="ad__mark"></span>
      <span class="ad__name">Daniel P. Harlow, DDS, PLLC</span>
      <span class="ad__tagline">Gentle care for every family</span>
    </div>
    <address class="ad__contact">
      <span>218 West Linden Street</span><br>
      <span>Millbrook</span><br>
      <span class="ad__phone">555-014-2290</span>
    </address>
  </article>

  <article class="ad ad--sky">
    <header class="ad__band">
      <h1 class="ad__headline">A Beautiful Smile</h1>
      <p class="ad__subhead">Today, It's Easier Than Ever</p>
    </header>
    <div class="ad__photo" role="img" aria-label="Photograph of a smiling older couple embracing, man in a blue shirt and woman in a coral top"></div>
    <div class="ad__practice">
      <span class="ad__mark"></span>
      <span class="ad__name">Daniel P. Harlow, DDS, PLLC</span>
      <span class="ad__tagline">Gentle care for every family</span>
    </div>
    <address class="ad__contact">
      <span>218 West Linden Street</span><br>
      <span>Millbrook</span><br>
      <span class="ad__phone">555-014-2290</span>
    </address>
  </article>
</main>
</body>
</html>
```